Flyer-Design für Aktionstag einer Teddy-Klinik gesucht
Zielgruppe
Ursprünglich ist die Teddyklinik eine Idee aus Schweden, doch inzwischen haben Fach-schaften in Deutschland an vielen medizinischen Universitäten diese Idee aufgenommen und umgesetzt. Seit einigen Jahren gibt es die Teddyklinik auch an der Universität zu Harvelsund, als AG der Fachschaft Medizin.
Aufgabenstellung
siehe Briefing-Dokument

```html
<!DOCTYPE html>
<html lang="de">
<head>
<meta charset="utf-8">
<title>Teddyklinik – Aktionstag Flyer</title>
<link href="https://fonts.googleapis.com/css2?family=Amatic+SC:wght@700&family=Caveat+Brush&family=Open+Sans:wght@400;700&display=swap" rel="stylesheet">
<style>
  :root {
    --page-bg: #eef1f3;
    --teal: #123f52;
    --red: #a61c2a;
    --sky: #bccbd5;
    --sky-light: #dfe6eb;
    --body-blue: #aebfcb;
    --url-band: #7f9bac;
    --white: #ffffff;
    --bear-dark: #8a6a4d;
    --bear-light: #c9b294;
  }
  * { margin: 0; padding: 0; box-sizing: border-box; }
  html, body { width: 1200px; height: 759px; overflow: hidden; }
  body { background: var(--page-bg); font-family: "Open Sans", sans-serif; }

  .flyer {
    position: absolute; left: 435px; top: 27px;
    width: 329px; height: 704px;
    background: var(--sky);
    overflow: hidden;
    box-shadow: 3px 4px 8px rgba(0,0,0,0.25);
  }

  .title {
    position: absolute; left: 26px; top: 20px;
    white-space: nowrap; line-height: 1; z-index: 3;
  }
  .title-teddy {
    font-family: "Amatic SC", sans-serif; font-weight: 700;
    font-size: 82px; color: var(--teal); letter-spacing: -1px;
  }
  .title-klinik {
    font-family: "Caveat Brush", cursive;
    font-size: 66px; color: var(--red); margin-left: 2px;
  }

  .date-band { position: absolute; left: 0; top: 0; width: 329px; height: 200px; z-index: 1; }
  .date-text {
    position: absolute; left: 180px; top: 110px; width: 148px;
    font-family: "Amatic SC", sans-serif; font-weight: 700;
    font-size: 25px; line-height: 1.05; color: var(--white);
    text-align: center; transform: rotate(-5deg); z-index: 3;
  }

  .bear-illustration {
    position: absolute; left: 27px; top: 90px; width: 150px; height: 228px;
    border-radius: 46% 46% 38% 38%;
    background: radial-gradient(circle at 50% 45%, var(--bear-light) 0%, var(--bear-dark) 72%);
    border: 4px solid var(--white);
    z-index: 2;
  }

  .free-band {
    position: absolute; left: 0; top: 268px; width: 329px; height: 52px;
    background: var(--sky-light);
  }
  .free-text {
    position: absolute; right: 27px; top: 5px;
    font-family: "Amatic SC", sans-serif; font-weight: 700;
    font-size: 20px; line-height: 1.1; color: var(--teal); text-align: center;
  }

  .venue-band {
    position: absolute; left: 0; top: 320px; width: 329px; height: 33px;
    background: var(--red); color: var(--white);
    font-weight: 700; font-size: 13.2px; text-align: center;
    line-height: 33px; white-space: nowrap; letter-spacing: 0.1px; z-index: 3;
  }

  .info {
    position: absolute; left: 0; top: 353px; width: 329px; height: 245px;
    background: var(--body-blue);
  }
  .info-column { position: absolute; top: 20px; width: 132px; text-align: center; color: var(--white); }
  .info-column--concept { left: 24px; }
  .info-column--process { left: 173px; }
  .info-heading {
    font-family: "Amatic SC", sans-serif; font-weight: 700;
    font-size: 23px; line-height: 1.05; color: var(--teal); margin-bottom: 14px;
  }
  .info-text { font-size: 8.4px; line-height: 11.4px; }
  .info-text strong { font-weight: 700; }

  .url-band {
    position: absolute; left: 0; top: 598px; width: 329px; height: 25px;
    background: var(--url-band); color: var(--white);
    font-weight: 700; font-size: 9.6px; text-align: center; line-height: 25px;
  }

  .footer {
    position: absolute; left: 0; top: 623px; width: 329px; height: 81px;
    background: var(--white);
    display: flex; align-items: center; justify-content: center; gap: 10px;
  }
  .footer-mark { width: 44px; height: 44px; border-radius: 50%; background: var(--teal); }
  .footer-name {
    font-weight: 700; font-size: 7.8px; letter-spacing: 1.2px;
    color: var(--teal); text-transform: uppercase;
  }
</style>
</head>
<body>
  <main class="flyer">
    <svg class="date-band" viewBox="0 0 329 200" aria-hidden="true">
      <polygon points="177,116 329,94 329,157 177,170" fill="#a61c2a"/>
    </svg>
    <div class="date-text">22.06.2019<br>10.00–16.00 UHR</div>

    <h1 class="title"><span class="title-teddy">TEDDY</span><span class="title-klinik">Klinik</span></h1>

    <div class="free-band">
      <p class="free-text">KOSTENLOS UND<br>OHNE ANMELDUNG</p>
    </div>

    <div class="bear-illustration" role="img" aria-label="Illustration: sitzender Teddybär mit Pflaster und Stethoskop"></div>

    <div class="venue-band">MARKTPLATZ AM RATHAUS IN HARVELSUND</div>

    <section class="info">
      <div class="info-column info-column--concept">
        <h2 class="info-heading">DAS KONZEPT<br>TEDDYKLINIK</h2>
        <p class="info-text">Kinder im Alter von <strong>3-6 Jahren</strong> sollen spielerisch an den Besuch beim Arzt und/oder an die Klinikuntersuchungen herangeführt werden. Hierfür kommen die Kinder mit ihren Lieblings-Kuscheltieren als „Patient“ zu uns und können den Arztbesuch beobachtend, aber auch interaktiv, mitverfolgen. So sollen Kinder die Furcht vor zukünftigen Arztbesuchen verlieren.</p>
      </div>
      <div class="info-column info-column--process">
        <h2 class="info-heading">ABLAUF<br>TEDDYKLINIK</h2>
        <p class="info-text">Rollenwechsel: In der Elternrolle kann das Kind den Besuch seines "Teddys" beim Doktor beobachten und mithelfen das Stofftier zu verarzten. Der Teddy wird während des Besuchs durch die Untersuchungen begleitet: von der Anmeldung über Röntgen/CT und den OP-Bereich bis hin zum Verbandszimmer. Die kleinen Teddyeltern helfen bei allen Behandlungen.</p>
      </div>
    </section>

    <div class="url-band">www.teddyklinik.uni-harvelsund.de</div>

    <footer class="footer">
      <span class="footer-mark" aria-hidden="true"></span>
      <span class="footer-name">Universität zu Harvelsund</span>
    </footer>
  </main>
</body>
</html>
```